Buff & Gleam

polished concrete and epoxy coatings flooring company

Target Market(s)

Industrial commercial

Industry/Entity Type

Industrial flooring contractor

Contact Information for Business Card

POLISHED CONCRETE • EPOXY COATING • TERRAZZO RESTORATION • SHOT BLASTING • SURFACE PREPARATION • JOINT FILLING • TILE/ CARPET /GLUE REMOVAL

Colors
0054AA
0677BA
7BADD7
CADEEF
E8F1F8

Requirements
Must have
• email buffandgleamfloors@mailbrook.example Address 47215 Tallowmere Rd, Corveth Falls, XR 90417. Name Ray Tulvin. Services Polished concrete- Epoxy Coatings- Terrazzo restoration-surface preparation- safety striping- joint filling- tile/ carpet/ glue removal phone number 555-700-3926 email buffandgleamfloors.example
Nice to have
• Instagram Facebook logo maybe smaller in the corner

```html
<!DOCTYPE html>
<html lang="en">
<head>
<meta charset="utf-8">
<title>Buff &amp; Gleam Business Card</title>
<link href="https://fonts.googleapis.com/css2?family=Oswald:wght@300;400;500;600;700&display=swap" rel="stylesheet">
<style>
  :root {
    --page: #ededee;
    --card-black: #1c1c1d;
    --brand-blue: #2479c4;
    --deep-blue: #0054aa;
    --silver: #c9cacc;
    --silver-dark: #8d8f92;
    --white: #ffffff;
    --ink: #111214;
  }
  * { box-sizing: border-box; margin: 0; padding: 0; }
  html, body { width: 1200px; height: 874px; overflow: hidden; }
  body {
    background: var(--page);
    font-family: "Oswald", "Arial Narrow", sans-serif;
    display: flex;
    flex-direction: column;
    align-items: center;
    justify-content: center;
    gap: 30px;
  }
  .card {
    position: relative;
    width: 700px;
    height: 400px;
    border-radius: 26px;
    overflow: hidden;
    background: var(--card-black);
    box-shadow: 0 6px 18px rgba(0,0,0,0.18);
  }

  /* Contact side */
  .card-info .divider { position: absolute; inset: 0; width: 100%; height: 100%; }
  .brand-block {
    position: absolute;
    left: 60px;
    top: 40px;
    width: 220px;
    text-align: center;
    color: var(--white);
  }
  .brand-name {
    font-size: 36px;
    font-weight: 500;
    letter-spacing: 1px;
    line-height: 1.05;
    text-transform: uppercase;
  }
  .brand-tagline {
    margin-top: 6px;
    font-size: 10px;
    font-weight: 600;
    letter-spacing: 1px;
    text-transform: uppercase;
  }
  .services {
    position: absolute;
    left: 70px;
    top: 150px;
    list-style: none;
    color: var(--white);
    font-size: 17px;
    font-weight: 300;
    line-height: 1.42;
  }
  .services li::before {
    content: "";
    display: inline-block;
    width: 6px; height: 6px;
    border-radius: 50%;
    background: var(--white);
    margin-right: 10px;
    vertical-align: middle;
  }
  .services strong { font-weight: 600; }

  .contact {
    position: absolute;
    right: 36px;
    top: 0;
    height: 100%;
    width: 300px;
    text-align: right;
    color: var(--white);
  }
  .person-name {
    margin-top: 70px;
    font-size: 50px;
    font-weight: 700;
    line-height: 1;
    text-transform: uppercase;
  }
  .person-role {
    font-size: 20px;
    font-weight: 300;
    font-style: italic;
    letter-spacing: 1px;
  }
  .address {
    margin-top: 26px;
    font-size: 18px;
    font-weight: 300;
    line-height: 1.25;
  }
  .address strong { font-weight: 600; }
  .phone {
    margin-top: 12px;
    font-size: 26px;
    font-weight: 700;
    display: flex;
    justify-content: flex-end;
    align-items: center;
    gap: 8px;
  }
  .email {
    margin-top: 2px;
    font-size: 14px;
    font-weight: 300;
    display: flex;
    justify-content: flex-end;
    align-items: center;
    gap: 8px;
  }
  .icon { width: 14px; height: 14px; flex: none; }
  .socials {
    position: absolute;
    right: 0;
    bottom: 22px;
    display: flex;
    gap: 18px;
    font-size: 11px;
    font-weight: 300;
    font-style: italic;
  }
  .social { display: flex; align-items: center; gap: 5px; }
  .social-dot {
    width: 11px; height: 11px;
    border-radius: 50%;
    background: var(--ink);
    display: inline-block;
  }

  /* Brand side */
  .card-brand .logo-block {
    position: absolute;
    left: 0; right: 0;
    top: 90px;
    text-align: center;
    color: var(--silver);
  }
  .card-brand .brand-name { font-size: 80px; font-weight: 500; letter-spacing: 3px; color: var(--silver); }
  .card-brand .brand-tagline { font-size: 20px; letter-spacing: 3px; color: var(--silver-dark); margin-top: 10px; }
  .web-band {
    position: absolute;
    left: 0; right: 0;
    bottom: 58px;
    height: 50px;
    background: var(--brand-blue);
    display: flex;
    align-items: center;
    justify-content: center;
    color: var(--ink);
    font-size: 26px;
    font-weight: 400;
  }
  .web-band strong { font-weight: 600; }
</style>
</head>
<body>

  <section class="card card-info" aria-label="Business card, contact side">
    <svg class="divider" viewBox="0 0 700 400" preserveAspectRatio="none" aria-hidden="true">
      <defs>
        <linearGradient id="silverLine" x1="0" y1="0" x2="0" y2="1">
          <stop offset="0" stop-color="#e6e7e8"/>
          <stop offset="1" stop-color="#6f7174"/>
        </linearGradient>
      </defs>
      <polygon points="418,0 700,0 700,400 352,400" fill="#2479c4"/>
      <polygon points="406,0 413,0 347,400 340,400" fill="url(#silverLine)"/>
    </svg>

    <div class="brand-block">
      <div class="brand-name">Buff &amp; Gleam</div>
      <div class="brand-tagline">Innovative Concrete Flooring</div>
    </div>

    <ul class="services">
      <li>Polished <strong>Concrete</strong></li>
      <li><strong>Epoxy</strong> Coatings</li>
      <li><strong>Terrazzo</strong> Restoration</li>
      <li>Surface <strong>Preparation</strong></li>
      <li>Safety <strong>Striping</strong></li>
      <li><strong>Joint</strong> Filling</li>
      <li>Tile/ <strong>Carpet</strong>/ Glue Removal</li>
    </ul>

    <div class="contact">
      <div class="person-name">Ray Tulvin</div>
      <div class="person-role">Owner Operator</div>
      <div class="address">47215 Tallowmere Rd,<br><strong>Corveth Falls, XR 90417</strong></div>
      <div class="phone">555-700-3926
        <svg class="icon" viewBox="0 0 24 24" aria-hidden="true"><path fill="#fff" d="M6.6 10.8a15 15 0 0 0 6.6 6.6l2.2-2.2a1 1 0 0 1 1-.25 11.4 11.4 0 0 0 3.6.6 1 1 0 0 1 1 1V20a1 1 0 0 1-1 1A17 17 0 0 1 3 4a1 1 0 0 1 1-1h3.5a1 1 0 0 1 1 1c0 1.250.2 2.45.6 3.6a1 1 0 0 1-.25 1z"/></svg>
      </div>
      <div class="email">buffandgleamfloors@mailbrook.example
        <svg class="icon" viewBox="0 0 24 24" aria-hidden="true"><circle cx="12" cy="12" r="10" fill="#fff"/><path d="M2 12h20M12 2c3 3 3 17 0 20M12 2c-3 3-3 17 0 20" stroke="#2479c4" stroke-width="1.5" fill="none"/></svg>
      </div>
      <div class="socials">
        <span class="social"><span class="social-dot"></span>@buffandgleamfloors</span>
        <span class="social"><span class="social-dot"></span>/buffandgleamfloors</span>
      </div>
    </div>
  </section>

  <section class="card card-brand" aria-label="Business card, brand side">
    <div class="logo-block">
      <div class="brand-name">Buff &amp; Gleam</div>
      <div class="brand-tagline">Innovative Concrete Flooring</div>
    </div>
    <div class="web-band">www.<strong>buffandgleamfloors</strong>.example</div>
  </section>

</body>
</html>
```